Bright Harbor Design

We need a web design for our startup company based in Zurich, Switzerland called Bright Harbor. We offer professional flirt and dating advice, self development with seminars and practical coachings.

The final website aims for two capital goals. First, it will contain text, pictures and video based content presenting and advertising our services. Furthermore, we want to bind our costumers with a plattform offering them to share their expiriences related with our services.

The targeted group will be men from 25 to 40 years.
Updates

The design requires also a register-box to put in the clients Name and Email

I need (besides of the "email registration box") a "Video Gallery", "Blog" and "Agenda (with the next events to come)"

Target Market(s)

Guys around 25 to 40 years who want to improve their social lifestyle

Industry/Entity Type

Advertising

Requirements
Must have
• First and foremost, the design must transfer strong emotions and suggest an attractive social lifestyle.

The design should not be overloaded with content but should include pictures, videos and text.

The design should present a modern, urban lifestyle.
Nice to have
• There is a logo attached to the assignement. However, if you have a good idea for an improved or different logo, please do not hesitate to design your ideas.

```html
<!DOCTYPE html>
<html lang="en">
<head>
<meta charset="utf-8">
<title>Bright Harbor</title>
<link rel="stylesheet" href="https://fonts.googleapis.com/css2?family=Raleway:wght@300;400;500;600&family=Open+Sans:wght@300;400;600&display=swap">
<style>
:root{
  --red:#d0121b;
  --red-dark:#a80f16;
  --black:#0b0b0b;
  --ink:#1a1a1a;
  --text:#555;
  --orange:#f2860c;
  --teal:#1aa5a0;
  --amber:#e08a0c;
  --field:#f3f3f3;
  --field-line:#e3e3e3;
  --rule:#dcdcdc;
  --grey-logo:#9a9a9a;
  --white:#fff;
}
*{box-sizing:border-box;margin:0;padding:0}
html,body{width:1175px;height:1200px;overflow:hidden;background:var(--white)}
body{position:relative;font-family:"Open Sans",Arial,sans-serif;color:var(--ink)}
.abs{position:absolute}

.brand{left:124px;top:44px;display:flex;align-items:center;gap:10px;font-family:"Raleway",Arial,sans-serif;font-weight:600;font-size:30px;color:var(--red);letter-spacing:.5px}
.brand-dot{width:22px;height:22px;border-radius:50%;background:var(--red)}

.btn-top{top:14px;height:33px;width:83px;font-family:"Raleway",Arial,sans-serif;font-weight:600;font-size:12.5px;color:var(--white);display:flex;align-items:center;justify-content:center;border-radius:3px}
.btn-signup{left:883px;background:var(--red)}
.btn-signin{left:972px;background:var(--black)}

.nav{top:77px;left:512px;width:546px;display:flex;justify-content:space-between;font-family:"Raleway",Arial,sans-serif;font-weight:500;font-size:15px;letter-spacing:2.2px;color:var(--black)}

.hero-photo{left:479px;top:101px;width:584px;height:378px;
  background:radial-gradient(ellipse at 60% 45%,#c99a78 0%,#dcbca4 30%,#eee6e0 55%,rgba(255,255,255,0) 75%),linear-gradient(180deg,#eef4f7,#fff)}
.hero-title{left:124px;top:164px;font-family:"Raleway",Arial,sans-serif;font-weight:300;font-size:36px;line-height:38px;letter-spacing:1px;color:var(--black);text-transform:uppercase;width:370px}
.btn-learn{left:124px;top:375px;width:158px;height:41px;background:var(--black);color:var(--white);font-family:"Raleway",Arial,sans-serif;font-weight:600;font-size:14px;letter-spacing:3px;display:flex;align-items:center;justify-content:center}

.tile{top:476px;width:301px;height:170px;border-radius:30px 0 30px 0;color:var(--white);display:flex;flex-direction:column;align-items:center;justify-content:center;text-align:center;font-family:"Raleway",Arial,sans-serif;font-weight:600;font-size:19px;line-height:24px;text-transform:uppercase;padding:0 20px}
.tile-teal{left:124px;background:linear-gradient(135deg,#14a19d,#2bb4ae 60%,#138f8b)}
.tile-amber{left:440px;background:linear-gradient(135deg,#d87c08,#e9960f 60%,#cf7706)}
.tile-red{left:754px;background:linear-gradient(135deg,#c80f18,#d8222a 55%,#9d0c13)}
.tile-big{font-weight:300;font-size:42px;line-height:46px}
.tile-small{font-size:15px;line-height:20px;margin-top:4px}

.h2{font-family:"Raleway",Arial,sans-serif;font-weight:300;font-size:30px;letter-spacing:.5px;color:var(--black);text-transform:uppercase}
.sub{font-size:14px;color:var(--black)}
.btn-share{left:575px;top:704px;width:134px;height:28px;background:#e6e6e6;font-family:"Raleway",Arial,sans-serif;font-weight:600;font-size:10px;letter-spacing:2.5px;display:flex;align-items:center;justify-content:center;color:var(--ink)}

.post{left:124px;width:590px;font-weight:300;font-size:13.5px;line-height:22.7px;color:var(--text)}
.more{color:var(--orange);font-weight:400;font-size:11px;text-transform:uppercase;margin-left:4px}

.label{left:754px;font-weight:300;font-size:14.5px;color:#444}
.field{height:32px;background:var(--field);border:1px solid var(--field-line);border-radius:2px}
.btn-send{left:919px;top:998px;width:137px;height:28px;background:var(--orange);color:var(--white);font-family:"Raleway",Arial,sans-serif;font-weight:600;font-size:10px;letter-spacing:2.5px;display:flex;align-items:center;justify-content:center}

.rule{left:124px;top:1103px;width:922px;height:1px;background:var(--rule)}
.foot-brand{left:126px;top:1130px;font-family:"Raleway",Arial,sans-serif;font-weight:600;font-size:20px;color:var(--grey-logo)}
.foot-links{right:129px;top:1145px;font-size:11px;color:var(--black)}
.foot-links span{margin:0 4px}
</style>
</head>
<body>
  <div class="abs brand"><span class="brand-dot"></span>Bright Harbor</div>
  <div class="abs btn-top btn-signup">SIGN UP</div>
  <div class="abs btn-top btn-signin">SIGN IN</div>
  <nav class="abs nav"><span>HOW IT WORKS</span><span>CONNECTIONS</span><span>VIDEOS</span><span>CONTACT US</span></nav>

  <div class="abs hero-photo" role="img" aria-label="Photo of a smiling couple at the beach, fading into white"></div>
  <h1 class="abs hero-title">Bright Harbor is exactly what you need to get your social life back on track</h1>
  <div class="abs btn-learn">LEARN MORE</div>

  <div class="abs tile tile-teal" role="img" aria-label="Teal-toned photo of friends on a city street">How can Bright Harbor get you back in the game</div>
  <div class="abs tile tile-amber" role="img" aria-label="Orange-toned photo of a couple in a shop">Share some of your Bright Harbor memories with us</div>
  <div class="abs tile tile-red" role="img" aria-label="Red-toned photo of a man at a table"><div class="tile-big">Videos</div><div class="tile-small">Check out some of our videos</div></div>

  <h2 class="abs h2" style="left:124px;top:696px">Connections</h2>
  <p class="abs sub" style="left:124px;top:732px">Past users Bright Harbor expereinces</p>
  <div class="abs btn-share">SHARE WITH US</div>

  <p class="abs post" style="top:774px">Lorem ipsum dolor sit amet, consectetur adipisicing elit, sed do eiusmod tempor incididunt ut labore et dolore magna aliqua. Ut enim ad minim veniam, quis nostrud exercitation ullamco laboris nisi ut aliquip ex ea commodo consequat. Duis aute irure dolor in reprehenderit in voluptate velit esse cillum dolore eu fugiat nulla pariatur. <span class="more">Read more</span></p>
  <p class="abs post" style="top:893px;width:580px">Lorem ipsum dolor sit amet, consectetur adipisicing elit, sed do eiusmod tempor incididunt ut labore et dolore magna aliqua. Ut enim ad minim veniam, quis nostrud exercitation ullamco laboris nisi ut aliquip ex ea commodo consequat. Duis aute irure dolor in reprehenderit <span class="more">Read more</span></p>
  <p class="abs post" style="top:994px;width:560px">Lorem ipsum dolor sit amet, consectetur adipisicing elit, sed do eiusmod tempor incididunt ut labore et dolore magna aliqua. Ut enim ad minim veniam, quis nostrud exercitation ullamco laboris nisi ut aliquip ex ea commodo consequat. <span class="more">Read more</span></p>

  <h2 class="abs h2" style="left:753px;top:696px">Register</h2>
  <p class="abs sub" style="left:753px;top:732px">It’s easy &amp; free to register, why not!</p>
  <div class="abs label" style="top:777px">Name</div>
  <div class="abs field" style="left:756px;top:801px;width:300px"></div>
  <div class="abs label" style="top:848px">Email</div>
  <div class="abs field" style="left:756px;top:873px;width:300px"></div>
  <div class="abs label" style="top:920px">Password</div>
  <div class="abs field" style="left:756px;top:944px;width:139px"></div>
  <div class="abs field" style="left:916px;top:944px;width:140px"></div>
  <div class="abs btn-send">SIGN ME UP</div>

  <div class="abs rule"></div>
  <div class="abs foot-brand">Bright Harbor</div>
  <div class="abs foot-links">© Bright Harbor<span>|</span>Privacy Policy<span>|</span>Terms of Use</div>
</body>
</html>
```